Vintage poster/postcard for 2011 New Years Eve event with theme 'Velvet Lanterns'

I have had a major change of mind since the last brief due to my original requirements being too specific. I hope this new brief allows more scope for the designers and I am extending the deadline by 7 days.

For the first time my new business 'Larkmoor Galas' is planning an exciting, large scale New Years Eve fundraising event in Hobart Tasmania, Australia. The unique and eclectic theme of the party is 'Velvet Lanterns' (french for contemporary circus). I require a vintage style poster design (similar to a traditional french advertising poster) that can double as a postcard invitation so it must look good on a smaller scale as well.
Updates

Project Deadline Extended
Reason: My original brief was very specific and I now realise very limiting for the designers. I have changed my mind with the look I want for the vintage poster (more along the lines of the traditional french advertising posters of old) and therefore would like to allow designers extra time to submit a design. Thank you. Dena Voss Larkmoor Galas

Target Market(s)

25-50 yr old professionals prepared to pay premium price for a quality, fresh & fun NYE experience while giving to charity.

Industry/Entity Type

Advertising

Requirements
Must have
• - A heading that reads: Larkmoor Galas proudly presents
Velvet Lanterns
- Text that includes: 2011 New Years Eve Extravanaganza Saturday 31st December and find out more at "www.larkmoorgalas.example
- A strip left blank at the bottom to include my business logo and others sponsors
- Classic french vintage poster design
- - Plenty of colour but not too fluro
- Something that looks good enough to be framed or sent to a friend
Should not have
• - Picture of Eiffel Tower or any other specific French references
- Any animals

```html
<!DOCTYPE html>
<html lang="en">
<head>
<meta charset="utf-8">
<title>Larkmoor Galas – Velvet Lanterns</title>
<link rel="stylesheet" href="https://fonts.googleapis.com/css2?family=Cinzel:wght@700;900&family=Macondo&display=swap">
<style>
  :root {
    --parchment: #cdb57e;
    --parchment-dark: #8e7442;
    --frame-ink: #3b2616;
    --stage-red: #6e241c;
    --stage-red-deep: #4a1611;
    --curtain: #c0634f;
    --gold: #c9a55e;
    --gold-light: #ecd59a;
    --cream: #f3e6c4;
    --outline: #2a170d;
    --plaque: #241710;
    --strip: #120c08;
  }
  * { margin: 0; padding: 0; box-sizing: border-box; }
  html, body { width: 849px; height: 1200px; overflow: hidden; background: var(--parchment); }

  .poster {
    position: relative;
    width: 849px;
    height: 1200px;
    overflow: hidden;
    background: radial-gradient(ellipse at center, #d8c28c 0%, var(--parchment) 60%, var(--parchment-dark) 100%);
  }

  .damask-border {
    position: absolute;
    inset: 0;
    background: radial-gradient(ellipse at center, rgba(0,0,0,0) 55%, rgba(90,60,25,0.35) 100%);
  }

  .outer-rule {
    position: absolute;
    inset: 12px;
    border: 3px solid var(--frame-ink);
  }

  .stage {
    position: absolute;
    left: 58px;
    top: 90px;
    width: 733px;
    height: 1072px;
    border-radius: 366px 366px 0 0 / 150px 150px 0 0;
    background:
      radial-gradient(ellipse 28% 55% at 50% 78%, var(--curtain) 0%, rgba(192,99,79,0.55) 50%, rgba(110,36,28,0) 100%),
      linear-gradient(90deg, var(--stage-red-deep) 0%, var(--stage-red) 18%, #7c2c22 50%, var(--stage-red) 82%, var(--stage-red-deep) 100%);
    box-shadow: inset 0 0 0 6px var(--frame-ink), inset 0 0 0 9px var(--gold);
  }

  .stage-arch {
    position: absolute;
    left: 0; top: 0;
    width: 849px; height: 1200px;
  }

  .plaque {
    position: absolute;
    left: 150px;
    top: 212px;
    width: 549px;
    height: 160px;
    border-radius: 80px;
    background: linear-gradient(180deg, #3a2619 0%, var(--plaque) 55%, #120b07 100%);
    border: 6px solid var(--gold);
    box-shadow: 0 0 0 3px var(--outline), inset 0 0 0 3px #6b4e2a;
    display: flex;
    flex-direction: column;
    align-items: center;
    justify-content: center;
    gap: 10px;
    text-align: center;
    color: var(--cream);
    font-family: 'Cinzel', serif;
    font-weight: 900;
    white-space: nowrap;
  }
  .plaque__name {
    display: block;
    font-size: 42px;
    line-height: 1;
    letter-spacing: 0.5px;
  }
  .plaque__presents {
    display: block;
    font-size: 30px;
    line-height: 1;
  }

  .title {
    position: absolute;
    left: 0;
    width: 849px;
    text-align: center;
    font-family: 'Macondo', cursive;
    font-weight: 400;
    color: var(--cream);
    -webkit-text-stroke: 4px var(--outline);
    paint-order: stroke fill;
    text-shadow: 5px 6px 0 var(--outline), 0 0 14px rgba(0,0,0,0.5);
    line-height: 1;
    text-transform: uppercase;
    white-space: nowrap;
  }
  .title--upper { top: 392px; font-size: 112px; letter-spacing: 2px; }
  .title--lower { top: 500px; font-size: 124px; letter-spacing: 0; }

  .tagline {
    position: absolute;
    left: 0;
    width: 849px;
    text-align: center;
    font-family: 'Cinzel', serif;
    font-weight: 900;
    color: var(--cream);
    -webkit-text-stroke: 3px var(--outline);
    paint-order: stroke fill;
    text-shadow: 3px 4px 0 var(--outline);
    line-height: 1;
    white-space: nowrap;
  }
  .tagline--year { top: 688px; font-size: 48px; letter-spacing: 1px; }
  .tagline--event { top: 742px; font-size: 48px; letter-spacing: 2px; }

  .details {
    position: absolute;
    left: 0;
    width: 849px;
    text-align: center;
    font-family: 'Cinzel', serif;
    color: #e3cf9e;
    line-height: 1;
    white-space: nowrap;
  }
  .details__date {
    top: 996px;
    font-size: 31px;
    font-weight: 900;
    text-shadow: 2px 2px 0 var(--outline);
  }
  .details__web {
    top: 1046px;
    font-size: 22px;
    font-weight: 700;
    letter-spacing: 1px;
    color: #e8d7ad;
  }

  .sponsor-strip {
    position: absolute;
    left: 88px;
    top: 1084px;
    width: 674px;
    height: 90px;
    border-radius: 30px;
    background: var(--strip);
  }
</style>
</head>
<body>
  <main class="poster">
    <div class="damask-border" role="img" aria-label="Aged parchment border with a faint floral damask pattern"></div>
    <div class="outer-rule"></div>

    <div class="stage" role="img" aria-label="Red theatre stage with draped velvet curtains beneath an ornate arch"></div>

    <svg class="stage-arch" viewBox="0 0 849 1200" aria-hidden="true">
      <path d="M40 1180 V240 Q40 70 424 60 Q809 70 809 240 V1180" fill="none" stroke="var(--frame-ink)" stroke-width="4"/>
      <path d="M30 1190 V236 Q30 58 424 48 Q819 58 819 236 V1190" fill="none" stroke="var(--gold)" stroke-width="2"/>
    </svg>

    <div class="plaque">
      <span class="plaque__name">LARKMOOR GALAS</span>
      <span class="plaque__presents">PROUDLY PRESENTS</span>
    </div>

    <h1>
      <span class="title title--upper">Velvet</span>
      <span class="title title--lower">Lanterns</span>
    </h1>

    <p class="tagline tagline--year">2011 NEW YEARS EVE</p>
    <p class="tagline tagline--event">EXTRAVAGANZA</p>

    <p class="details details__date">SATURDAY 31ST DECEMBER</p>
    <p class="details details__web">WWW.LARKMOORGALAS.EXAMPLE</p>

    <div class="sponsor-strip"></div>
  </main>
</body>
</html>
```